Pest Control Company needs business card!

Hi there, we need a business card designed for our new Pest Control Company. Ideally this card will be simple, yet feel elegant and high end. We want to use the colours Orange, Black and White. Please see our attached logo for the exact colours.

Business card details:

Phone - 0461 275 804
Name - Gavin Holloway
Email - Info@steadfastverminguard.com.au

We would also like to include the following list with dot points:

SERVICES / INSPECTIONS

Termites, Wood Borers, Ants, Cockroaches, Spiders, Fleas, Mice, Rats, Bed Bugs, & More!

```html
<!DOCTYPE html>
<html lang="en">
<head>
<meta charset="utf-8">
<title>Steadfast Vermin Guard – Business Card</title>
<link rel="stylesheet" href="https://fonts.googleapis.com/css2?family=Montserrat:wght@400;500;600;800&display=swap">
<style>
  :root {
    --stage: #d9d9d9;
    --card-black: #231f20;
    --brand-red: #e30d17;
    --brand-orange: #e07318;
    --ink-white: #ffffff;
  }
  * { box-sizing: border-box; margin: 0; padding: 0; }
  html, body {
    width: 1200px; height: 800px; overflow: hidden;
    background: var(--stage);
    font-family: "Montserrat", Arial, sans-serif;
  }
  .stage {
    width: 1200px; height: 800px;
    display: flex; align-items: center; justify-content: center; gap: 40px;
  }
  .card {
    position: relative;
    width: 540px; height: 309px;
    background: var(--card-black);
    overflow: hidden;
    box-shadow: 0 6px 18px rgba(0,0,0,.18);
  }

  /* Front side */
  .front .red-band {
    position: absolute; left: 0; right: 0; bottom: 0; height: 138px;
    background: var(--brand-red);
  }
  .front .brand-lockup {
    position: absolute; top: 40px; left: 44px; right: 36px;
    display: flex; align-items: center; justify-content: space-between;
  }
  .brand-dot {
    width: 92px; height: 92px; border-radius: 50%;
    background: var(--brand-orange);
  }
  .brand-name {
    font-weight: 800; color: var(--brand-orange);
    text-transform: uppercase; line-height: 1.02; letter-spacing: .5px;
  }
  .front .brand-name { font-size: 30px; text-align: right; }
  .contact {
    position: absolute; left: 44px; bottom: 26px; color: var(--ink-white);
  }
  .contact .person-name {
    font-weight: 800; font-size: 20px; text-transform: uppercase;
    letter-spacing: .5px; margin-bottom: 6px;
  }
  .contact .detail { font-size: 12.5px; font-weight: 400; line-height: 1.35; }
  .website {
    position: absolute; right: 30px; top: 190px;
    color: var(--ink-white); font-size: 12px; font-weight: 400;
  }

  /* Back side */
  .back .brand-lockup {
    position: absolute; top: 56px; left: 0; right: 0;
    display: flex; align-items: center; justify-content: center; gap: 22px;
  }
  .back .brand-name { font-size: 34px; }
  .services {
    position: absolute; left: 0; right: 0; bottom: 34px;
    color: var(--ink-white); text-align: center;
    font-size: 13.5px; font-weight: 500; text-transform: uppercase;
    line-height: 1.55; letter-spacing: .3px;
  }
  .services .sep { color: var(--brand-red); margin: 0 6px; }
</style>
</head>
<body>
<main class="stage">
  <section class="card front" aria-label="Business card front">
    <div class="red-band"></div>
    <div class="brand-lockup">
      <span class="brand-dot" aria-hidden="true"></span>
      <p class="brand-name">Steadfast<br>Vermin<br>Guard</p>
    </div>
    <div class="contact">
      <p class="person-name">Gavin Holloway</p>
      <p class="detail">0461 275 804</p>
      <p class="detail">Info@steadfastverminguard.com.au</p>
    </div>
    <p class="website">www.steadfastverminguard.com.au</p>
  </section>

  <section class="card back" aria-label="Business card back">
    <div class="brand-lockup">
      <p class="brand-name">Steadfast<br>Vermin<br>Guard</p>
      <span class="brand-dot" aria-hidden="true"></span>
    </div>
    <div class="services">
      <p>Termites<span class="sep">•</span>Wood Borers<span class="sep">•</span>Ants<span class="sep">•</span>Cockroaches</p>
      <p>Spiders<span class="sep">•</span>Fleas<span class="sep">•</span>Mice<span class="sep">•</span>Rats<span class="sep">•</span>Bed Bugs &amp; More</p>
    </div>
  </section>
</main>
</body>
</html>
```